Family Owned and Operated Spray Foam Insulation Company needs a business card design

We're a new company based in the heart of Texas (Fort Worth). We spray foam insulation into residential houses, commercial buildings, metal buildings, etc. Spray foam insulation provides a huge reduction in energy/costs so that is what drives our market. We like the primary colors but are open to suggestions and are coming to the experts for some creativity. I'm attaching a picture of shirt mock up we have with KLB on the front to show what we were leaning towards as well as some business cards that I find striking and memorable. I'm looking for a card that is clean and professional with a bit of edge. Note: My computer won't pull up the color samples below for me to choose so it's in your hands.

Target Market(s)

Professional custom home builders, construction industry, home owners

Industry/Entity Type

Residential

Contact Information for Business Card

Name: Marcus Kettle (no title) Phone #: 817-555-0148, address: 4087 larkmoor ave fort worth tx 76110, email: marcus@klbinsulation-example.com, website: klbinsulation-example.com

Requirements
Must have
• We want the words KLB and Kettle Spray Foam Insulation showcased on the card but hopefully on opposite sides
Should not have
• Any type of spray foam gun or splatter clip art

```html
<!DOCTYPE html>
<html lang="en">
<head>
<meta charset="utf-8">
<title>Kettle Spray Foam Insulation – Business Card</title>
<link rel="stylesheet" href="https://fonts.googleapis.com/css2?family=PT+Sans:wght@400;700&display=swap">
<style>
  :root {
    --backdrop: #ffffff;
    --paper: #ecebe8;
    --paper-edge: #dcdad6;
    --brand-teal: #1b7aa3;
    --name-blue: #2269a0;
    --ink-navy: #263551;
  }
  html, body {
    margin: 0;
    padding: 0;
    width: 1200px;
    height: 918px;
    overflow: hidden;
    background: var(--backdrop);
  }
  .canvas {
    position: relative;
    width: 1200px;
    height: 918px;
    display: flex;
    flex-direction: column;
    align-items: center;
    justify-content: center;
    gap: 48px;
    font-family: "PT Sans", sans-serif;
  }
  .card {
    position: relative;
    width: 630px;
    height: 360px;
    background: var(--paper);
    border: 1px solid var(--paper-edge);
    border-radius: 4px;
    box-sizing: border-box;
  }
  .card-back {
    display: flex;
    flex-direction: column;
    align-items: center;
    justify-content: center;
    gap: 18px;
  }
  .brand-mark {
    font-weight: 700;
    color: var(--brand-teal);
    letter-spacing: 2px;
    line-height: 1;
  }
  .card-back .brand-mark {
    font-size: 140px;
  }
  .company-name {
    margin: 0;
    font-size: 24px;
    font-weight: 700;
    color: var(--name-blue);
    letter-spacing: 1px;
    line-height: 1.2;
  }
  .card-front .brand-mark {
    position: absolute;
    top: 42px;
    left: 0;
    right: 0;
    text-align: center;
    font-size: 78px;
  }
  .holder-name {
    position: absolute;
    top: 150px;
    left: 0;
    right: 0;
    margin: 0;
    text-align: center;
    font-size: 40px;
    font-weight: 700;
    color: var(--name-blue);
    letter-spacing: 0.5px;
    line-height: 1.2;
  }
  .contact-list {
    position: absolute;
    top: 232px;
    left: 292px;
    margin: 0;
    padding: 0;
    list-style: none;
    font-size: 16px;
    line-height: 20px;
    color: var(--ink-navy);
    white-space: nowrap;
  }
</style>
</head>
<body>
  <main class="canvas">
    <section class="card card-back" aria-label="Card back">
      <span class="brand-mark">KLB</span>
      <p class="company-name">Kettle Spray Foam Insulation</p>
    </section>

    <section class="card card-front" aria-label="Card front">
      <span class="brand-mark">KLB</span>
      <h1 class="holder-name">Marcus Kettle</h1>
      <ul class="contact-list">
        <li>p: 817-555-0148</li>
        <li>e: marcus@klbinsulation-example.com</li>
        <li>w: klbinsulation-example.com</li>
        <li>a: 4087 larkmoor ave fort worth tx 76110</li>
      </ul>
    </section>
  </main>
</body>
</html>
```